Health & Fitness Author & Public Speaker Needs Visually Stunning Web Redesign!

It's time for a redesign of the home page for Verity Halloway's "Bright Fork Kitchen" website (www.brightforkkitchen-example.com). We have a VERY clear idea of what we want, so it really won't take a talented designer long to bring it to life.
The website itself is used to promote & sell her range of health & nutrition programs to a female audience, primarily aged 24 - 35 working in professional or semi professional occupations.
For a VERY comprehensive outline of exactly what we are after, please see the following attached files:
(1) 'Website - WireFrame' (layout, content/copy, visual design style we want along with the desired color scheme)
(2) 'Website - Style Guide' (these are the colours, and overall feel we want)
PLEASE REVIEW THIS IN FULL - THEY WILL GIVE YOU A VERY CLEAR IDEA OF WHAT WE WANT.
Most of the files you need are attached, but for more photos that you can use (of Verity, her programs, and food/meals) can be found at these URL's:
VERITY (profile photos):
https://www.filebinbox.example/sh/qm3rt8wpz1xkd7a/RtPlm4vaNe
ECOVERS
- Bright Fork Kitchen Guide (ebook): https://www.filebinbox.example/sh/wxtnvo5d274ku22/hBqYrsnoz3
- 21 Week Total Momentum Course (ecourse): https://www.filebinbox.example/sh/zopqinr6a2mhwyl/c-dg341oTR
- E-Magazine Issues:
https://www.filebinbox.example/sh/4pzmkar2s9vtyw/57LeWcdDxpB
STOCK IMAGES:
https://www.filebinbox.example/sh/k2qowr8atbnzlx/Qe3HT5mmDy
As we will need to revamp our existing Facebook page & other printed material, there may be the potential for further work for the successful designer in the future.
Thanks & Good Luck!
Declan Furrow
Marketing & Business Development Manager
Bright Fork Kitchen

```html
<!DOCTYPE html>
<html lang="en">
<head>
<meta charset="utf-8">
<title>Bright Fork Kitchen – Home</title>
<link href="https://fonts.googleapis.com/css2?family=Oswald:wght@400;500&family=Open+Sans:wght@400;600;700&display=swap" rel="stylesheet">
<style>
:root{
  --purple:#9c0f9a;
  --purple-dark:#7d0b7c;
  --pink:#e8175d;
  --ink:#333;
  --muted:#8a8a8a;
  --band:#2f2f2f;
  --panel:#efefef;
  --white:#fff;
  --red:#e0201c;
}
*{box-sizing:border-box;margin:0;padding:0}
html,body{width:720px;height:1200px;overflow:hidden;background:var(--white)}
body{position:relative;font-family:"Open Sans",Arial,sans-serif;color:var(--ink)}
.abs{position:absolute}
.photo{position:absolute}
.hero{left:0;top:0;width:720px;height:352px;background:linear-gradient(115deg,#b9c3c9 0%,#8e9aa3 30%,#d8c0a8 55%,#6f7a84 80%,#c9b29a 100%)}
.header{left:40px;top:10px;width:640px;height:59px;background:rgba(255,255,255,.96);box-shadow:0 1px 3px rgba(0,0,0,.15)}
.logo{left:10px;top:18px;font-family:"Open Sans",sans-serif;font-weight:700;font-size:15px;color:var(--purple);display:flex;align-items:center;gap:6px}
.logo i{display:block;width:10px;height:10px;border-radius:50%;background:var(--purple)}
.contact{right:14px;top:14px;font-size:9.5px;font-style:italic;font-weight:600;color:#444;display:flex;gap:14px}
.contact span{display:flex;align-items:center;gap:4px}
.nav{right:10px;top:34px;display:flex;font-family:"Oswald",sans-serif;font-size:10.5px;color:#333}
.nav a{color:inherit;text-decoration:none;padding:5px 13px;height:25px}
.nav a.active{background:var(--purple);color:var(--white)}
.header .rule{left:0;bottom:0;width:100%;height:2px;background:var(--purple)}
.headline{left:432px;font-family:"Oswald",sans-serif;font-weight:500;font-size:28px;color:var(--white);background:rgba(60,60,60,.82);width:248px;height:38px;line-height:38px;padding-left:10px;letter-spacing:.3px}
.signup{left:42px;top:301px;width:638px;height:51px;background:var(--white)}
.signup .pitch{left:0;top:0;width:224px;height:51px;background:var(--purple);color:var(--white);padding:7px 12px}
.pitch h3{font-family:"Oswald",sans-serif;font-weight:400;font-size:11.5px}
.pitch p{font-size:8px;line-height:10px;margin-top:3px}
.field-label{font-size:7px;color:var(--muted)}
.field{border:1px solid #ccc;background:var(--white);height:18px}
.hook{left:568px;top:1px;width:70px;height:18px;background:var(--purple);color:var(--white);font-size:9px;text-align:center;line-height:18px;font-weight:600}
.hero-rule{left:0;top:352px;width:720px;height:3px;background:var(--purple)}
h2.section{font-family:"Oswald",sans-serif;font-weight:400;color:var(--purple);font-size:14px}
.copy{font-size:7.2px;line-height:12.6px;color:var(--muted);text-align:justify}
.video{overflow:hidden}
.video .frame{position:absolute;left:0;top:0;width:100%;height:calc(100% - 18px)}
.video .play{position:absolute;left:50%;top:50%;width:28px;height:24px;margin:-18px 0 0 -14px;background:var(--red);border-radius:4px}
.video .play:after{content:"";position:absolute;left:11px;top:6px;border-left:9px solid #fff;border-top:6px solid transparent;border-bottom:6px solid transparent}
.video .bar{position:absolute;left:0;bottom:0;width:100%;height:18px;background:#1b1b1b}
.video .track{position:absolute;left:0;top:0;width:100%;height:3px;background:#555}
.video .track b{display:block;height:3px;width:52%;background:var(--red)}
.video .time{position:absolute;left:36px;top:6px;font-size:5.5px;color:#ddd}
.book-cta{left:75px;top:868px;font-family:"Oswald",sans-serif;font-weight:500;font-size:19px;color:var(--purple)}
.side-box{left:496px;width:182px;background:var(--panel);box-shadow:0 4px 4px -2px rgba(0,0,0,.2)}
.side-box h4{font-family:"Oswald",sans-serif;font-weight:400;color:var(--purple);font-size:12px;padding:8px 9px 0}
.socials{display:flex;gap:9px;padding:7px 11px}
.socials i{display:block;width:19px;height:19px;border-radius:50%;background:#3a3a3a;border:2px solid #cfcfcf}
.socials i:first-child{background:#2b6fb6}
.search{display:flex;margin:9px 11px 0;height:18px}
.search .field{flex:1;font-size:6.5px;color:var(--muted);padding:4px 6px}
.search .go{width:20px;background:var(--purple)}
.promo{left:496px;width:182px;overflow:hidden}
.promo-order h5{position:absolute;left:9px;top:5px;font-family:"Oswald",sans-serif;font-weight:500;font-size:19px;color:var(--white)}
.promo-order p{position:absolute;left:11px;top:31px;font-size:8px;line-height:10px;color:#222;width:100px}
.promo-order .buy{position:absolute;left:13px;top:56px;font-family:"Oswald",sans-serif;font-size:11px;color:#f5c400}
.promo-free .caption{position:absolute;left:0;bottom:0;width:100%;height:52px;background:rgba(30,30,30,.85);padding:6px 7px;color:var(--white)}
.caption h6{font-family:"Oswald",sans-serif;font-weight:400;font-size:10.5px}
.caption p{font-size:8px;line-height:12px;margin-top:2px}
.caption .free{position:absolute;right:5px;top:3px;writing-mode:vertical-rl;font-family:"Oswald",sans-serif;font-weight:500;font-size:15px;color:#e61bd6}
.band{left:0;top:912px;width:720px;height:182px;background:var(--band)}
.band h2{position:absolute;left:167px;top:12px;font-family:"Oswald",sans-serif;font-weight:400;color:var(--white);font-size:15px}
.band .sub{position:absolute;left:168px;top:36px;font-size:7px;color:#bbb}
.band .field-label{color:#999}
.band .field{background:#2b2b2b;border-color:#555}
.band .send{position:absolute;left:208px;top:148px;width:170px;height:18px;background:var(--pink);color:var(--white);font-size:7px;text-align:center;line-height:18px}
.partners{left:0;top:1094px;width:720px;height:64px;display:flex;justify-content:space-around;align-items:center;font-family:"Oswald",sans-serif;font-weight:500;color:#333;font-size:15px}
.partners span:last-child{color:var(--purple)}
.footer{left:0;top:1158px;width:720px;height:42px;background:var(--purple);color:var(--white);text-align:center}
.footer nav{font-size:8px;padding-top:9px}
.footer nav a{color:#f0d6ef;text-decoration:none;margin:0 5px}
.footer nav a:first-child{color:var(--white);font-weight:700}
.footer p{font-size:7px;color:#e9c9e8;margin-top:6px}
</style>
</head>
<body>

<div class="photo hero" role="img" aria-label="Woman in yellow sports top doing sit-ups in a bright gym"></div>

<header class="abs header">
  <div class="abs logo"><i></i>Bright Fork Kitchen</div>
  <div class="abs contact">
    <span><svg width="9" height="9" viewBox="0 0 10 10"><path d="M2 1l2 2-1 1.5c.6 1.2 1.3 1.9 2.5 2.5L7 6l2 2-1.3 1.3C4.5 9 1 5.5.7 2.3z" fill="#e8175d"/></svg>012 555 0148</span>
    <span><svg width="10" height="8" viewBox="0 0 10 8"><rect x=".5" y=".5" width="9" height="7" fill="none" stroke="#e8175d"/><path d="M.5.5L5 4.5 9.5.5" fill="none" stroke="#e8175d"/></svg>info@brightforkkitchen-example.com</span>
  </div>
  <nav class="abs nav">
    <a class="active">HOME</a><a>ABOUT VERITY</a><a>THE MAGAZINE</a><a>BLOG &amp; VIDEOS</a><a>SHOP</a><a>CONTACT US</a>
  </nav>
  <div class="abs rule"></div>
</header>

<div class="abs headline" style="top:138px">GET SLIM BOOST</div>
<div class="abs headline" style="top:178px">ENERGY GUILT FREE</div>

<form class="abs signup">
  <div class="abs pitch">
    <h3>Join the BRIGHT BODY WELLNESS Movement!</h3>
    <p>A weekly serving of motivation, recipes &amp; FREE resources straight to your inbox! Email Icon</p>
  </div>
  <div class="abs field-label" style="left:245px;top:13px">Enater your name :</div>
  <div class="abs field" style="left:245px;top:27px;width:136px"></div>
  <div class="abs field-label" style="left:412px;top:13px">Enater your email :</div>
  <div class="abs field" style="left:412px;top:27px;width:136px"></div>
  <div class="abs hook">Hook me up!</div>
  <svg class="abs" style="left:568px;top:20px" width="70" height="30" viewBox="0 0 70 30"><path d="M0 0h70v30H0z" fill="#9c0f9a"/><path d="M2 2l33 17L68 2M2 28l24-13M68 28L44 15" fill="none" stroke="#fff" stroke-width="3"/></svg>
</form>
<div class="abs hero-rule"></div>

<main>
  <h2 class="abs section" style="left:40px;top:381px">How to Handle Bright Fork Kitchen</h2>
  <p class="abs copy" style="left:40px;top:405px;width:426px">Lorem ipsum dolor sit amet, consectetur adipiscing elit. Suspendisse sagittis varius diam, eu gravida elit hendrerit at. Proin nec porta mauris, tincidunt lacinia est. Vestibulum lobortis dictum sapien ut tincidunt. Fusce semper egas iaculis. Vestibulum in pulvinar odio. Mauris non pretium felis. Mauris quam sapien, porta sit amet vehicula sed, dapibus in enim. Morbi pharetra neque eget eros ultricies dictum. Quisque sem leo, auctor vitae accumsan sed, vulputate scelerisque lectus.</p>
  <p class="abs copy" style="left:40px;top:460px;width:426px">Vestibulum non ultricies purus. Fusce eu metus a leo iaculis congue. Fusce laoreet est ut vehicula consat. Maecenas pharetra, lacus et sagittis luctus, lacus erat tristique ipsum, sed commodo dui nibh a elit. Praesent fermentum tempus felis, at sagittis nunc blandit nec. Ut sit amet massa et urna mollis molestie ac condimentum diam. Mauris nec solldin purus. Nulla vulputate, lectus ac pretium tincidunt, nunc nulla cursus purus, in dictum est augue sit amet nisi. Interdum et malesuada fames ac ante ipsum primis in faucibus. Etiam pretium id erat eu venenatis. Suspendisse consectetur a purus sed aliquam. Fusce dapibus purus eu turpis lobortis eleifend. Aliquam eget leo a erat feugiat dignissim id id lorem.</p>

  <div class="abs video" style="left:42px;top:550px;width:201px;height:154px">
    <div class="frame" role="img" aria-label="Video still of two women in a fitness studio" style="background:linear-gradient(135deg,#5d4f4f,#8c7a7a 50%,#4a4242)"></div>
    <div class="play"></div>
    <div class="bar"><div class="track"><b></b></div><span class="time">0:14 / 0:38</span></div>
  </div>
  <div class="abs video" style="left:262px;top:550px;width:202px;height:154px">
    <div class="frame" role="img" aria-label="Video still of a woman eating watermelon against a grey wall" style="background:linear-gradient(135deg,#3e4448,#5c6468 60%,#8a8f90)"></div>
    <div class="play"></div>
    <div class="bar"><div class="track"><b></b></div><span class="time">0:14 / 0:38</span></div>
  </div>

  <div class="photo" style="left:42px;top:724px;width:211px;height:140px;background:linear-gradient(135deg,#c9b1c7,#e7dde3 45%,#a8c9a0 75%,#d9b6a3)" role="img" aria-label="Stack of healthy eating books and magazines"></div>
  <div class="abs book-cta">Book order now</div>

  <h2 class="abs section" style="left:264px;top:718px">Our books nd Lectures</h2>
  <p class="abs copy" style="left:264px;top:738px;width:201px">Lorem ipsum dolor sit amet, consectetur adipiscing elit. Suspendisse sagittis varius diam, eu gravida elit hendrerit at. Proin nec porta mauris, tincidunt lacinia est. Vestibulum lobortis dictum sapien ut tincidunt. Fusce semper egas iaculis. Vestibulum in pulvinar odio. Mauris non pretium felis. Mauris quam sapien, porta sit amet vehicula sed, dapibus in enim.</p>
  <p class="abs copy" style="left:264px;top:830px;width:201px">Gravida elit hendrerit at. Proin nec porta mauris, tincidunt lacinia est. Vestibulum lobortis dictum sapien ut tincidunt. Fusce semper egas iaculis. Vestibulum in pulvinar odio. Mauris non pretium felis. Mauris quam sapien, porta sit amet vehicula sed, dapibus in enim.</p>
</main>

<aside>
  <section class="abs side-box" style="top:386px;height:60px">
    <h4>Followes with Bright Fork Kitchen</h4>
    <div class="socials"><i></i><i></i><i></i><i></i><i></i><i></i></div>
  </section>
  <section class="abs side-box" style="top:464px;height:60px">
    <h4>Search Bright Fork Kitchen</h4>
    <div class="search"><div class="field">Search</div><div class="go"><svg width="20" height="18" viewBox="0 0 20 18"><circle cx="9" cy="8" r="4" fill="none" stroke="#fff" stroke-width="1.6"/><path d="M12 11l3 3" stroke="#fff" stroke-width="1.8"/></svg></div></div>
  </section>
  <section class="abs promo promo-order" style="top:541px;height:145px">
    <div class="photo" style="left:0;top:0;width:182px;height:145px;background:linear-gradient(135deg,#8fa0ab,#b7c3ca 55%,#d8c6b8)" role="img" aria-label="Woman holding watermelon beside program covers"></div>
    <h5>Order Today</h5>
    <p>Get free coaching and guided meditations</p>
    <div class="buy">★ Buy now ★</div>
  </section>
  <section class="abs promo promo-free" style="top:704px;height:184px">
    <div class="photo" style="left:0;top:0;width:182px;height:184px;background:linear-gradient(160deg,#6f8f4a,#a3b86d 45%,#5a6e3a)" role="img" aria-label="Woman sitting on grass holding an apple"></div>
    <div class="caption">
      <h6>GET SLIM BOOST ENERGY GUILT</h6>
      <p>Ultimate 30 Day Kick Start<br>Program + Detox</p>
      <span class="free">FREE</span>
    </div>
  </section>
</aside>

<section class="abs band">
  <div class="photo" style="left:40px;top:0;width:124px;height:182px;background:linear-gradient(180deg,#5a3a2e,#b08a74 40%,#7b3f9a 80%)" role="img" aria-label="Portrait of Verity in a purple top"></div>
  <h2>Want to feel better today?</h2>
  <div class="sub">Join the BRIGHT BODY WELLNESS Movement!</div>
  <div class="abs field-label" style="left:208px;top:62px">Enater your name :</div>
  <div class="abs field" style="left:208px;top:73px;width:170px"></div>
  <div class="abs field-label" style="left:208px;top:104px">Enater your email :</div>
  <div class="abs field" style="left:208px;top:115px;width:170px"></div>
  <div class="send">SING UP ME</div>
  <div class="abs video" style="left:432px;top:12px;width:248px;height:158px">
    <div class="frame" role="img" aria-label="Video still of a woman stretching against a brick wall" style="background:linear-gradient(135deg,#8d8a80,#c2bdb0 45%,#6e6a62)"></div>
    <div class="play"></div>
    <div class="bar"><div class="track"><b></b></div><span class="time">0:14 / 0:38</span></div>
  </div>
</section>

<div class="abs partners">
  <span>Solmere</span><span>Radiant Stride</span><span>Maison Lune</span><span>Core Daily</span>
</div>

<footer class="abs footer">
  <nav><a>Home</a>/<a>About Verity</a>/<a>The Magazine</a>/<a>Blog &amp; Videos</a>/<a>Shop</a>/<a>Contact Us</a></nav>
  <p>Copyright © 2014 brightforkkitchen-example.com. All rights reserved</p>
</footer>

</body>
</html>
```